Ads for Law Firm

I am an employment lawyer who represents individual employees. I currently have a banner ad on sites focused on individual employment rights, like ShiftBalanceWatch.org and TrelloviaCounsel.com. I am looking for an ad that incorporates best practices for promoting a professional service.

I am attaching a couple of existing ads that I want to replace. The new ad should be the same dimension as the attached. The old ad is a friend helped with, and focuses on my great credentials.

I have read that people looking for lawyers care a less about credentials, and more about whether the lawyer can protect them. It should also have a call to action, being to call or email me. Therefore, the ad should say something like "call [me/Otto] to protect your [job/employment/rights/etc],"

Industry/Entity Type

Lawyer

```html
<!DOCTYPE html>
<html lang="en">
<head>
<meta charset="utf-8">
<title>Otto Brennholt – Employment Lawyer Banner</title>
<link rel="stylesheet" href="https://fonts.googleapis.com/css2?family=Signika:wght@600;700&family=Arimo:wght@400;700&display=swap">
<style>
  :root {
    --page-bg: #ffffff;
    --band-dark: #1c1c1c;
    --band-mid: #2a2a2a;
    --portrait-light: #d9dadc;
    --portrait-mid: #9a9ea4;
    --chevron-light: #e4e4e4;
    --chevron-shade: #b9b9b9;
    --name-white: #ffffff;
    --cta-yellow: #f2c21b;
    --firm-bg: #0f3147;
    --firm-text: #ffffff;
    --caption-ink: #111111;
  }
  html, body {
    margin: 0;
    padding: 0;
    width: 1200px;
    height: 394px;
    overflow: hidden;
    background: var(--page-bg);
  }
  .canvas {
    position: relative;
    width: 1200px;
    height: 394px;
  }
  .banner {
    position: absolute;
    left: 43px;
    top: 46px;
    width: 1133px;
    height: 146px;
    background: linear-gradient(180deg, var(--band-mid), var(--band-dark));
    overflow: hidden;
  }
  .banner__portrait {
    position: absolute;
    left: 0;
    top: 0;
    width: 230px;
    height: 146px;
    background: radial-gradient(ellipse at 45% 40%, var(--portrait-light), var(--portrait-mid));
  }
  .banner__chevron {
    position: absolute;
    left: 200px;
    top: 0;
    width: 110px;
    height: 146px;
  }
  .banner__name {
    position: absolute;
    left: 312px;
    top: 13px;
    margin: 0;
    font-family: "Signika", sans-serif;
    font-weight: 700;
    font-size: 50px;
    line-height: 1;
    color: var(--name-white);
    text-shadow: 2px 2px 2px #000;
    letter-spacing: 0.5px;
    white-space: nowrap;
  }
  .banner__cta {
    position: absolute;
    left: 314px;
    top: 87px;
    margin: 0;
    font-family: "Arimo", sans-serif;
    font-weight: 700;
    font-size: 30px;
    line-height: 1;
    color: var(--cta-yellow);
    white-space: nowrap;
  }
  .banner__firm {
    position: absolute;
    right: 0;
    top: 0;
    width: 187px;
    height: 146px;
    background: var(--firm-bg);
    display: flex;
    align-items: center;
    justify-content: center;
    text-align: center;
    font-family: "Signika", sans-serif;
    font-weight: 700;
    font-size: 30px;
    line-height: 1.1;
    color: var(--firm-text);
  }
  .caption {
    position: absolute;
    left: 58px;
    top: 232px;
    margin: 0;
    width: 1100px;
    font-family: "Arimo", sans-serif;
    font-size: 30px;
    line-height: 43px;
    color: var(--caption-ink);
  }
</style>
</head>
<body>
<main class="canvas">
  <section class="banner" aria-label="Otto Brennholt employment lawyer banner">
    <div class="banner__portrait" role="img" aria-label="Portrait photo of the lawyer in a suit"></div>
    <svg class="banner__chevron" viewBox="0 0 110 146" aria-hidden="true">
      <polygon points="0,0 52,0 104,73 52,146 0,146 48,73" fill="var(--chevron-light)"/>
      <polygon points="52,0 104,73 98,73 46,0" fill="var(--chevron-shade)"/>
    </svg>
    <h1 class="banner__name">Otto Brennholt</h1>
    <p class="banner__cta">Call Otto to Protect Your Job!</p>
    <div class="banner__firm">Brennholt<br>Law</div>
  </section>
  <p class="caption">* Animated banner ad, please check the description link to see<br>&nbsp;the animation in action</p>
</main>
</body>
</html>
```